Home page graphic design only (NOT WEBSITE DESIGN)

I require a home page to be designed for my new website.
I DO NOT REQUIRE to build a website. We are a rug company specialising in alpaca wool. It is targeted at the high end of the market and hence the graphics of our page requires to reflect this. Our current page is as per attachment and I think it is too basic.
Updates

Target Market(s)

Extremly high net worth individuals where luxury is a requirement

Requirements
Must have
• show of style, luxury, uniqueness. Prefer having bright images.
Nice to have
• a highly sofisticated roomscape where the focus in the rug. See attachment as an example
Should not have
• Not sure

```html
<!DOCTYPE html>
<html lang="en">
<head>
<meta charset="utf-8">
<title>Velours Andin – Home</title>
<link rel="stylesheet" href="https://fonts.googleapis.com/css2?family=Libre+Baskerville&family=Quicksand:wght@400;500&display=swap">
<style>
  :root{
    --board:#dfcc98;
    --ink:#000;
    --paper:#fff;
    --gold:#e3b838;
    --gold-soft:#c9a33a;
    --text:#1c1c1c;
    --weave-red:#b8321c;
    --weave-dark:#6e1a0e;
  }
  html,body{margin:0;padding:0;width:1200px;height:884px;overflow:hidden;background:var(--board);font-family:'Quicksand',sans-serif;}
  .page{position:absolute;left:327px;top:22px;width:546px;height:819px;background:var(--paper);overflow:hidden;}
  .header{position:absolute;left:0;top:0;width:546px;height:206px;background:var(--ink);}
  .weave-corner{position:absolute;left:0;top:0;}
  .nav{position:absolute;top:6px;left:0;width:546px;display:flex;justify-content:center;gap:11px;font-size:9px;color:var(--paper);}
  .nav span{padding:1px 4px;}
  .nav .current{background:var(--gold);color:var(--ink);}
  .title{position:absolute;top:30px;left:0;width:546px;padding-left:36px;box-sizing:border-box;text-align:center;font-family:'Libre Baskerville',serif;font-size:46px;color:var(--gold);margin:0;font-weight:400;}
  .established{position:absolute;left:221px;top:96px;font-size:11px;color:var(--paper);}
  .brand-mark{position:absolute;left:30px;top:80px;display:flex;align-items:center;gap:5px;color:var(--gold);font-size:10px;font-weight:500;}
  .brand-mark i{display:block;width:14px;height:14px;border-radius:50%;background:var(--gold);}
  .alpaca{position:absolute;left:171px;top:82px;width:203px;height:212px;border-radius:40% 40% 8% 8%;background:radial-gradient(ellipse at 50% 55%,#6a6a6a,#1e1e1e 70%);}
  .company{position:absolute;left:0;top:221px;width:137px;height:27px;background:var(--ink);color:var(--gold);font-size:8.5px;line-height:11px;text-align:center;padding-top:3px;box-sizing:border-box;}
  .social{position:absolute;left:370px;top:221px;width:176px;height:27px;background:var(--ink);display:flex;align-items:center;justify-content:space-around;padding:0 4px;box-sizing:border-box;}
  .social span{background:var(--gold);color:var(--ink);font-size:7px;font-weight:500;border-radius:4px;padding:5px 3px;}
  .headline{position:absolute;top:320px;left:0;width:546px;text-align:center;font-size:22px;line-height:28px;color:var(--text);margin:0;font-weight:400;}
  .headline em{font-style:normal;color:var(--gold-soft);}
  .tile-label{position:absolute;width:140px;text-align:center;font-size:12.5px;color:var(--text);}
  .tile{position:absolute;width:114px;height:114px;}
  .tile-collections{left:108px;top:427px;background:linear-gradient(135deg,#1f3d9a,#d22a1f 45%,#f0b41e 70%,#1f3d9a);}
  .tile-story{left:322px;top:427px;background:linear-gradient(160deg,#9a8a5a,#6f7a2e 55%,#4b3a2a);}
  .tile-news{left:110px;top:575px;background:linear-gradient(180deg,#c9a98a,#eee6dc 55%,#a0704a);}
  .tile-publications{left:322px;top:575px;background:linear-gradient(135deg,#111 25%,#7a6252 50%,#d6d2cc 80%);}
  .regions{position:absolute;left:0;top:735px;width:546px;height:35px;background:linear-gradient(90deg,var(--weave-red),var(--weave-dark) 50%,var(--weave-red));color:var(--paper);font-size:19px;font-weight:500;text-align:center;line-height:35px;}
  .footer{position:absolute;left:0;top:794px;width:546px;height:14px;background:var(--ink);color:var(--paper);font-size:6.3px;text-align:center;line-height:14px;}
</style>
</head>
<body>
<div class="page">
  <header class="header">
    <svg class="weave-corner" width="546" height="206" viewBox="0 0 546 206" role="img" aria-label="Andean woven textile pattern in red, orange and black">
      <defs>
        <linearGradient id="weave" x1="0" y1="1" x2="1" y2="0">
          <stop offset="0" stop-color="#6e1a0e"/>
          <stop offset="0.5" stop-color="#b8321c"/>
          <stop offset="1" stop-color="#d8632a"/>
        </linearGradient>
      </defs>
      <polygon points="546,0 369,206 546,206" fill="url(#weave)"/>
    </svg>
    <nav class="nav">
      <span class="current">Home</span><span>Collections</span><span>Our Story</span><span>About us</span><span>FAQ</span><span>Publications</span><span>News &amp; Events</span><span>Contact us</span>
    </nav>
    <h1 class="title">Velours Andin</h1>
    <div class="brand-mark"><i></i>Velours Andin</div>
    <div class="established">established in 1988</div>
  </header>
  <div class="alpaca" role="img" aria-label="Engraved black and white illustration of a standing alpaca"></div>
  <div class="company">Velours Andin Pty Ltd<br>ABN 12 345 6/7 890</div>
  <div class="social"><span>Share</span><span>Watch</span><span>Post</span><span>Photo</span><span>Map</span></div>
  <h2 class="headline">Exquisite luxury carpeting and arca rugs made<br>from pure <em>Peruvian Alpaca</em></h2>
  <div class="tile-label" style="left:95px;top:403px;">Collections</div>
  <div class="tile tile-collections" role="img" aria-label="Close-up of a brightly patterned rug in red, blue and yellow"></div>
  <div class="tile-label" style="left:309px;top:403px;">Our Story</div>
  <div class="tile tile-story" role="img" aria-label="Alpaca being fed in a grassy field"></div>
  <div class="tile-label" style="left:97px;top:550px;">News &amp; Events</div>
  <div class="tile tile-news" role="img" aria-label="Banquet hall with patterned carpet and dressed tables"></div>
  <div class="tile-label" style="left:309px;top:549px;">Publications</div>
  <div class="tile tile-publications" role="img" aria-label="Rug with curved bands of black, brown and grey"></div>
  <div class="regions" role="img" aria-label="Woven textile band">AUSTRALIA ~ USA ~ EUROPE ~ ASIA ~ UAE</div>
  <footer class="footer">Copyright ©2020 Velours Andin - Australia - Head Office - Suite 8 / Unit 114 _ Riverbend Road; Riverbend VIC 3999</footer>
</div>
</body>
</html>
```